Vitamin Company Website Design

Seeking to create a vibrant and professional looking website for a vitamin and health food supplements business.

Morning Flintroot is a company that develops and sells vitamins and supplements for those following the "paleo" or "caveman" diet. The diet focuses upon eating organic vegetables and meat, like our ancient ancestors.

The website should emphasize health and wellness. A clean and bold design is preferred.

The website should include four sections: a home page, a blog, a community forum and an e-commerce store.

These websites communicate what we would like to look like:

http://www.korvelstudio.example/
http://www.unityassembly.example/
http://www.tlx.example/
http://www.zestkitten.example/
http://openvoiceforum.example/en/
http://tastebayoucatch.example/
http://buyrooted.example/

Target Market(s)

Health conscious men and women age 25-50

Industry/Entity Type

E-Commerce

Requirements
Must have
• The website must have 4 pages: home page, blog, community forum and online store.

The website must incorporate the company's logo, which is attached.

The company's green logo with the tagline: "Fresh Roots. Steady Mornings." is the preferred logo.

Please incorporate the other logo graphics where you see fit.
Nice to have
• Ideally, the designer will add images and/or graphics that compliment a website dedicated to health and wellness.

```html
<!DOCTYPE html>
<html lang="en">
<head>
<meta charset="utf-8">
<title>Morning Flintroot</title>
<link href="https://fonts.googleapis.com/css2?family=Asap:wght@400;500&display=swap" rel="stylesheet">
<style>
:root{
  --green:#44b649;
  --green-line:#8fd093;
  --grey-panel:#ebebec;
  --grey-bar:#a7a8aa;
  --ink:#1e1e1e;
  --white:#ffffff;
  --logo-grey:#7d7f82;
}
*{margin:0;padding:0;box-sizing:border-box}
html,body{width:1200px;height:900px;overflow:hidden;background:var(--white)}
body{position:relative;font-family:"Asap",Arial,sans-serif;color:var(--ink)}
.abs{position:absolute}

/* hero mosaic */
.brand-tile{left:187px;top:3px;width:327px;height:162px;background:var(--green)}
.brand-tile .mark{position:absolute;left:10px;top:50px;width:62px;height:62px;border-radius:50%;background:var(--white)}
.brand-tile .name{position:absolute;left:82px;top:62px;font-size:27px;font-weight:500;color:var(--white);white-space:nowrap}
.brand-tile .tagline{position:absolute;right:12px;top:96px;font-size:9px;color:var(--white);white-space:nowrap}
.photo{width:163px;height:162px}
.photo.peppers{left:519px;top:3px;background:radial-gradient(circle at 55% 40%,#f17a1c,#d8331a 60%,#7d9a3a)}
.photo.milk{left:685px;top:3px;background:linear-gradient(180deg,#f2f2f0,#e6e3d6 55%,#bdbdbd)}
.photo.tomatoes{left:851px;top:3px;width:163px;background:radial-gradient(circle at 60% 35%,#e4442a,#5f8b2c 55%,#e2b35a)}
.photo.salmon{left:187px;top:169px;background:linear-gradient(160deg,#f2f0ec,#d8774e 45%,#4f7a2e 70%,#f0ede6)}
.photo.honey{left:353px;top:169px;background:linear-gradient(180deg,#5b5c6a,#3d3e4a 45%,#f3a21b)}
.photo.fruit{left:519px;top:169px;background:radial-gradient(circle at 45% 50%,#e3362c,#c9b93a 50%,#f2882d)}
.photo.cutlery{left:685px;top:169px;background:linear-gradient(135deg,#ffffff,#e6e6e6 50%,#b9b9bb)}
.photo.olives{left:851px;top:169px;width:163px;background:radial-gradient(circle at 55% 45%,#e5c04a,#9a9a2c 55%,#6b4f2a)}

/* intro */
.intro{left:187px;top:336px;width:659px;height:159px;background:var(--grey-panel)}
.intro p{position:absolute;left:34px;top:48px;width:600px;font-size:11.8px;line-height:19px}
.social{left:852px;top:336px;width:162px;height:159px;background:var(--green);color:var(--white);text-align:center}
.social h2{margin-top:17px;font-size:17px;font-weight:400}
.social .icons{display:flex;justify-content:center;gap:17px;margin-top:21px}
.social .icon{width:42px;height:42px;border-radius:6px}
.social .icon.one{background:#3b5a9a}
.social .icon.two{background:#39b7e6}
.social small{display:block;margin-top:17px;font-size:11px}

/* site header */
.main-nav{left:0;top:514px;width:1200px;height:22px}
.main-nav a{position:absolute;font-size:11.5px;color:var(--ink);text-decoration:none;transform:translateX(-50%);white-space:nowrap}
.main-nav .active::after{content:"";position:absolute;left:-16px;right:-16px;top:19px;height:2px;background:var(--green)}
.site-logo{left:193px;top:528px;height:36px}
.site-logo .mark{position:absolute;left:0;top:0;width:36px;height:36px;border-radius:50%;background:var(--logo-grey)}
.site-logo .name{position:absolute;left:42px;top:7px;font-size:15px;font-weight:500;color:var(--logo-grey);white-space:nowrap}
.site-logo .tagline{position:absolute;left:90px;top:26px;font-size:5px;color:var(--logo-grey);white-space:nowrap}
.header-bar{left:375px;top:545px;width:639px;height:8px;background:var(--grey-bar)}

/* columns */
.col-title{top:579px;font-size:11px;font-weight:400;letter-spacing:.2px}
.col-rule{top:602px;width:1px;height:220px;background:var(--green-line)}
.small-copy{font-size:7.6px;line-height:19px}
.post-photo{left:219px;top:623px;width:102px;height:67px;background:linear-gradient(135deg,#d9c7b3,#e58aa6 45%,#f3efe8)}
.post-title{left:334px;top:650px;font-size:11px;line-height:19px}
.post-body{left:219px;top:694px;width:232px}
.forum-body{left:481px;top:613px;width:245px}
.replies-title{left:481px;top:717px;font-size:11px}
.replies-body{left:481px;top:731px;width:245px}
.product{left:761px;width:66px;height:66px;border:1px solid var(--ink);display:flex;align-items:center;justify-content:center}
.pill{width:50px;height:18px;border-radius:9px}
.pill.capsule{background:linear-gradient(180deg,#fbf9f2,#e2ddcd)}
.pill.tablet{width:42px;height:22px;border-radius:50%;background:radial-gradient(circle at 40% 40%,#f8c24a,#e89a1a)}
.pill.softgel{width:36px;height:24px;border-radius:50%;background:radial-gradient(circle at 40% 40%,#fdf6d8,#c9b67a)}
.product-copy{left:837px;width:160px}
.price{left:837px;font-size:11px}

/* footer */
.footer{left:183px;top:834px;width:833px;height:64px;background:var(--green);color:var(--white)}
.footer-nav{position:absolute;left:182px;top:24px;font-size:11px;display:flex;align-items:center}
.footer-nav a{color:var(--white);text-decoration:none}
.footer-nav .sep{display:inline-block;width:1px;height:11px;background:var(--white);margin:0 17px}
.footer .contact-label{position:absolute;left:679px;top:15px;font-size:8px}
.footer .divider{position:absolute;left:719px;top:14px;width:1px;height:46px;background:var(--white)}
.footer .contact-list{position:absolute;left:728px;top:13px;font-size:8px;line-height:13.5px}
</style>
</head>
<body>

<header>
  <div class="abs brand-tile">
    <span class="mark"></span>
    <span class="name">Morning Flintroot</span>
    <span class="tagline">Fresh Roots. Steady Mornings.</span>
  </div>
  <div class="abs photo peppers" role="img" aria-label="Bowl of red and orange peppers with sliced mushrooms"></div>
  <div class="abs photo milk" role="img" aria-label="Glass of milk"></div>
  <div class="abs photo tomatoes" role="img" aria-label="Tomatoes and basil on dried pasta"></div>
  <div class="abs photo salmon" role="img" aria-label="Grilled salmon steak with asparagus"></div>
  <div class="abs photo honey" role="img" aria-label="Honey dripping from a dipper into a jar"></div>
  <div class="abs photo fruit" role="img" aria-label="Fresh fruit salad with strawberries and kiwi"></div>
  <div class="abs photo cutlery" role="img" aria-label="Fork and knife on a white plate"></div>
  <div class="abs photo olives" role="img" aria-label="Bottle of olive oil with green olives"></div>
</header>

<section class="abs intro">
  <p>Morning Flintroot.....Lorem ipsum dolor sit amet, consectetuer adipiscing elit, sed diam nonummy nibh euismod tincidunt ut laoreet dolore magna aliquam erat volutpat. Ut wisi enim ad minim veniam, quis nostrud exerci tation ullamcorper suscipit lobortis nisl ut aliquip ex ea commodo consequat.</p>
</section>

<aside class="abs social">
  <h2>Find us on</h2>
  <div class="icons"><span class="icon one"></span><span class="icon two"></span></div>
  <small>social media icons</small>
</aside>

<nav class="abs main-nav">
  <a href="#" style="left:460px">home</a>
  <a href="#" class="active" style="left:540px">blog</a>
  <a href="#" style="left:650px">community forum</a>
  <a href="#" style="left:779px">e-commerce</a>
</nav>
<div class="abs site-logo">
  <span class="mark"></span>
  <span class="name">Morning Flintroot</span>
  <span class="tagline">Fresh Roots. Steady Mornings.</span>
</div>
<div class="abs header-bar"></div>

<main>
  <h3 class="abs col-title" style="left:224px">BLOG</h3>
  <h3 class="abs col-title" style="left:481px">COMMUNITY FORUM</h3>
  <h3 class="abs col-title" style="left:762px">E-COMMERCE</h3>
  <div class="abs col-rule" style="left:459px"></div>
  <div class="abs col-rule" style="left:740px"></div>

  <div class="abs post-photo" role="img" aria-label="Two women sharing a meal at a table"></div>
  <div class="abs post-title">BLOG POST<br>TITLE HERE</div>
  <p class="abs small-copy post-body">Lorem ipsum dolor sit amet, consectetuer adipiscing elit, sed diam nonummy nibh euismod tincidunt ut laoreet dolore magna aliquam erat volutpat. Ut wisi enim ad minim veniam, quis nostrud exerci tation ullamcorper suscipit lobortis nisl ut aliquip ex ea commodo consequat.</p>

  <p class="abs small-copy forum-body">Lorem ipsum dolor sit amet, consectetuer adipiscing elit, sed diam nonummy nibh euismod tincidunt ut laoreet dolore magna aliquam erat volutpat. Ut wisi enim ad minim veniam, quis nostrud exerci tation ullamcorper suscipit lobortis nisl ut aliquip ex ea commodo consequat.</p>
  <h4 class="abs replies-title" style="font-weight:400">REPLIES</h4>
  <p class="abs small-copy replies-body">.Lorem ipsum dolor sit amet, consectetuer adipiscing elit, sed diam nonummy nibh euismod tincidunt ut laoreet dolore magna aliquam erat volutpat. Ut wisi enim ad minim veniam, quis nostrud exerci tation ullamcorper suscipit lobortis nisl ut aliquip ex ea commodo consequat.</p>

  <div class="abs product" style="top:610px"><span class="pill capsule" role="img" aria-label="White capsule supplement"></span></div>
  <p class="abs small-copy product-copy" style="top:611px">Lorem ipsum dolor sit amet, consectetuer adipiscing elit,</p>
  <span class="abs price" style="top:660px">$123</span>

  <div class="abs product" style="top:683px"><span class="pill tablet" role="img" aria-label="Orange tablet supplement"></span></div>
  <p class="abs small-copy product-copy" style="top:683px">Lorem ipsum dolor sit amet, consectetuer adipiscing elit,</p>
  <span class="abs price" style="top:733px">$123</span>

  <div class="abs product" style="top:755px"><span class="pill softgel" role="img" aria-label="Clear softgel supplement"></span></div>
  <p class="abs small-copy product-copy" style="top:752px">Lorem ipsum dolor sit amet, consectetuer adipiscing elit,</p>
  <span class="abs price" style="top:805px">$123</span>
</main>

<footer class="abs footer">
  <nav class="footer-nav">
    <a href="#">home</a><span class="sep"></span>
    <a href="#">blog</a><span class="sep"></span>
    <a href="#">community forum</a><span class="sep"></span>
    <a href="#">e-commerce</a>
  </nav>
  <span class="contact-label">contact</span>
  <span class="divider"></span>
  <div class="contact-list">(555) 010-4471<br>info@flintroot.example<br>other important links</div>
</footer>

</body>
</html>
```